Project Meridel PowerPoint Design

This is a PPT design for Power & Utilities company who are in the process of a technology upgrade for their Finance department. We are looking to develop a branded PPT for Project Meridel (specifically MERIDEL). Why does Meridel resonate? "The Earth is pointed almost directly at Meridel. During the course of the night,
Meridel does not rise or set, but remains in nearly the same spot above the
northern horizon year- round while the other stars circle around it."
Meridel represents the guiding principles that manage, monitor and
control the organizations financials.

Target Market(s)

Finance stakeholders impacted by technology enhancement

Font styles to use
Serif
Other font styles liked:
• Arial

Colors
0054AA
0677BA
7BADD7
CADEEF
E8F1F8

Requirements
Must have
• Various slide layout ( Cover slide, content slide, divider, etc). Attached is the logo and corporate colors
Nice to have
• Over the top creativity

```html
<!DOCTYPE html>
<html lang="en">
<head>
<meta charset="utf-8">
<title>Project Meridel – Presentation Design</title>
<link href="https://fonts.googleapis.com/css2?family=Arimo:wght@400;700&family=Montserrat:wght@500&display=swap" rel="stylesheet">
<style>
:root{
  --navy:#1e3a8f;
  --bar-light:#4a72d9;
  --slate:#76787b;
  --paper:#ececec;
  --ink:#1d1d1f;
  --white:#ffffff;
  --stripe:#8a8c90;
}
*{box-sizing:border-box;margin:0;padding:0}
html,body{width:1200px;height:3654px;overflow:hidden;background:var(--white);font-family:Arimo,Arial,sans-serif;color:var(--ink)}
.slide{position:absolute;left:98px;width:985px;height:553px;overflow:hidden;background:var(--paper)}
.s-cover{top:56px}.s-service{top:638px}.s-feature{top:1223px}.s-chart{top:1809px;background:var(--navy)}
.s-pillars{top:2397px}.s-close{top:2985px}
.shape{position:absolute;left:0;top:0;width:985px;height:553px}
.photo{position:absolute}
.wordmark{position:absolute;color:var(--white);font-family:Montserrat,Arial,sans-serif;font-weight:500;text-align:center;line-height:1}
.wordmark .wm-small{display:block;font-size:27px;letter-spacing:9px;margin-bottom:6px}
.wordmark .wm-large{display:block;font-size:64px;letter-spacing:6px}
.tagline{position:absolute;left:0;width:985px;top:312px;text-align:center;color:var(--white);font-size:20px;line-height:30px}
.service-box{position:absolute;left:14px;top:39px;width:479px;height:463px;background:var(--slate);color:var(--white);padding:128px 30px 0 29px}
.service-box h2{font-size:40px;font-weight:700;margin-bottom:12px;letter-spacing:.5px}
.service-box p{font-size:11.5px;line-height:23px;margin-bottom:8px}
.service-item{position:absolute;width:220px;text-align:center}
.service-item .badge{display:block;margin:0 auto 14px;width:90px;height:90px}
.service-item h3{color:var(--navy);font-size:12.5px;font-weight:700;margin-bottom:10px}
.service-item p{font-size:10px;line-height:16px}
.feature-copy{position:absolute;left:29px;top:112px;width:430px}
.feature-copy h2{font-size:40px;line-height:48px;font-weight:700;letter-spacing:.5px;margin-bottom:22px}
.feature-copy h3{color:var(--navy);font-size:16px;font-weight:700;margin-bottom:8px}
.feature-copy p{font-size:10px;line-height:18px;margin-bottom:24px}
.chart-title{position:absolute;left:0;width:985px;top:56px;text-align:center;color:var(--white);font-size:38px;font-weight:700;letter-spacing:1px}
.section-title{position:absolute;left:0;width:985px;top:38px;text-align:center;color:var(--navy);font-size:40px;font-weight:700;letter-spacing:.5px}
.pillar{position:absolute;width:240px}
.pillar.left{text-align:right}
.pillar h3{color:var(--navy);font-size:12px;line-height:17px;font-weight:700;margin-bottom:5px}
.pillar p{font-size:9.5px;line-height:14px;color:#555}
.thanks{position:absolute;left:513px;top:200px;width:440px;color:var(--white)}
.thanks h2{font-size:44px;font-weight:700;margin-bottom:14px}
.thanks p{font-size:13.5px;line-height:23px}
</style>
</head>
<body>

<!-- Cover -->
<section class="slide s-cover">
  <div class="photo" role="img" aria-label="Photograph of business people reviewing financial charts at a desk" style="left:0;top:0;width:985px;height:553px;background:linear-gradient(135deg,#2f3740 0%,#545b64 55%,#7a8088 100%)"></div>
  <svg class="shape" viewBox="0 0 985 553" aria-hidden="true">
    <polygon points="0,0 830,0 798,72 0,72" fill="var(--stripe)"/>
    <polygon points="0,0 812,0 780,72 0,72" fill="var(--navy)"/>
    <polygon points="150,481 985,481 985,553 118,553" fill="var(--stripe)"/>
    <polygon points="168,481 985,481 985,553 136,553" fill="var(--navy)"/>
  </svg>
  <div class="wordmark" style="left:0;width:985px;top:188px">
    <span class="wm-small">PROJECT</span>
    <span class="wm-large">MERIDEL</span>
  </div>
  <p class="tagline">Nemo enim ipsam voluptatem quia voluptas sit aspernatur aut<br>odit aut fugit, sed quia consequuntur magni.</p>
</section>

<!-- Service -->
<section class="slide s-service">
  <svg class="shape" viewBox="0 0 985 553" aria-hidden="true">
    <polygon points="0,0 452,0 432,36 0,36" fill="var(--stripe)"/>
    <polygon points="0,0 432,0 412,36 0,36" fill="var(--navy)"/>
    <polygon points="378,481 985,481 985,553 416,553" fill="var(--stripe)"/>
    <polygon points="398,481 985,481 985,553 436,553" fill="var(--navy)"/>
  </svg>
  <div class="service-box">
    <h2>SERVICE</h2>
    <p>Perspiciatis unde omnis iste natus error sit voluptatem accusantium doloremque laudantium, totam rem aperiam, eaque ipsa quae ab illo inventore veritatis et quasi architecto beatae vitae dicta sunt explicabo.</p>
    <p>Nemo enim ipsam voluptatem quia voluptas sit aspernatur aut odit aut fugit, sed quia consequuntur magni dolores eos qui ratione voluptatem sequi nesciunt. Neque porro quisquam est, qui dolorem ipsum quia dolor sit amet, consectetur.</p>
  </div>

  <div class="service-item" style="left:505px;top:50px">
    <svg class="badge" viewBox="0 0 90 90" aria-hidden="true"><circle cx="45" cy="45" r="45" fill="var(--navy)"/><g fill="none" stroke="#fff" stroke-width="2"><path d="M28 24h22l8 8v34H28z"/><circle cx="52" cy="56" r="9"/><path d="M52 51v10M49 53h5M49 59h5"/><path d="M36 34l-3 7h5l-3 7"/></g></svg>
    <h3>Service Heading</h3>
    <p>Nemo enim ipsam voluptatem quia voluptas sit aspernatur aut odit aut fugit, sed quia consequuntur magni dolores dolorem ipsum quia dolor sit amet, consectetur</p>
  </div>
  <div class="service-item" style="left:760px;top:50px">
    <svg class="badge" viewBox="0 0 90 90" aria-hidden="true"><circle cx="45" cy="45" r="45" fill="var(--navy)"/><g fill="none" stroke="#fff" stroke-width="2"><circle cx="45" cy="36" r="6"/><circle cx="33" cy="44" r="5"/><circle cx="57" cy="44" r="5"/><path d="M34 62v-8a11 11 0 0 1 22 0v8z"/><path d="M24 62v-5a9 9 0 0 1 9-9M66 62v-5a9 9 0 0 0-9-9"/><path d="M45 20v5M36 23l2 4M54 23l-2 4"/></g></svg>
    <h3>Service Heading</h3>
    <p>Nemo enim ipsam voluptatem quia voluptas sit aspernatur aut odit aut fugit, sed quia consequuntur magni dolores dolorem ipsum quia dolor sit amet, consectetur</p>
  </div>
  <div class="service-item" style="left:505px;top:266px">
    <svg class="badge" viewBox="0 0 90 90" aria-hidden="true"><circle cx="45" cy="45" r="45" fill="var(--navy)"/><g fill="none" stroke="#fff" stroke-width="2"><circle cx="36" cy="40" r="6"/><path d="M24 64v-8a12 12 0 0 1 24 0v8z"/><path d="M40 32l10-8 6 5 10-8M62 21h4v4"/><rect x="52" y="48" width="14" height="16"/><path d="M52 53h14M52 58h14"/></g></svg>
    <h3>Service Heading</h3>
    <p>Nemo enim ipsam voluptatem quia voluptas sit aspernatur aut odit aut fugit, sed quia consequuntur magni dolores dolorem ipsum quia dolor sit amet, consectetur</p>
  </div>
  <div class="service-item" style="left:760px;top:266px">
    <svg class="badge" viewBox="0 0 90 90" aria-hidden="true"><circle cx="45" cy="45" r="45" fill="var(--navy)"/><g fill="none" stroke="#fff" stroke-width="2"><path d="M36 52a14 14 0 1 1 18 0v6H36z"/><path d="M38 63h14M40 67h10"/><circle cx="45" cy="42" r="5"/><path d="M45 16v5M27 24l3 3M63 24l-3 3M20 42h5M65 42h5"/></g></svg>
    <h3>Service Heading</h3>
    <p>Nemo enim ipsam voluptatem quia voluptas sit aspernatur aut odit aut fugit, sed quia consequuntur magni dolores dolorem ipsum quia dolor sit amet, consectetur</p>
  </div>
</section>

<!-- Feature -->
<section class="slide s-feature">
  <svg class="shape" viewBox="0 0 985 553" aria-hidden="true">
    <polygon points="0,0 817,0 785,71 0,71" fill="var(--stripe)"/>
    <polygon points="0,0 799,0 767,71 0,71" fill="var(--navy)"/>
    <polygon points="735,481 985,481 985,553 767,553" fill="var(--stripe)"/>
    <polygon points="753,481 985,481 985,553 785,553" fill="var(--navy)"/>
  </svg>
  <div class="photo" role="img" aria-label="Photograph of an engineer in a hard hat holding a tablet beside a power transmission tower" style="left:481px;top:45px;width:479px;height:465px;background:linear-gradient(160deg,#7d9cc2 0%,#a9c0d8 45%,#c49a6a 100%)"></div>
  <div class="feature-copy">
    <h2>EXCEPTEUR SINT<br>OCCAECAT</h2>
    <h3>Excepteur sint occaecat cupidatat</h3>
    <p>Nemo enim ipsam voluptatem quia voluptas sit aspernatur aut odit aut fugit, sed quia consequuntur magni dolores dolorem ipsum quia dolor sit amet, consectetur, adipisci velit tempor incididunt ut labore et dolore magna perspiciatis unde omnis iste natus error sit voluptatem accusantium doloremque laudantium, totam rem aperiam.</p>
    <h3>Excepteur sint occaecat cupidatat</h3>
    <p>Nemo enim ipsam voluptatem quia voluptas sit aspernatur aut odit aut fugit, sed quia consequuntur magni dolores dolorem ipsum quia dolor sit amet, consectetur, adipisci velit tempor incididunt ut labore et dolore magna perspiciatis unde omnis iste natus error sit voluptatem accusantium doloremque laudantium, totam rem aperiam.</p>
  </div>
</section>

<!-- Chart -->
<section class="slide s-chart">
  <h2 class="chart-title">NEMO ENIM IPSAM</h2>
  <svg class="shape" viewBox="0 0 985 553" role="img" aria-label="Bar chart of yearly values from 2012 to 2021">
    <g stroke="#6f86c4" stroke-width="1">
      <line x1="186" y1="144" x2="840" y2="144"/><line x1="186" y1="180" x2="840" y2="180"/>
      <line x1="186" y1="216" x2="840" y2="216"/><line x1="186" y1="252" x2="840" y2="252"/>
      <line x1="186" y1="287" x2="840" y2="287"/><line x1="186" y1="323" x2="840" y2="323"/>
      <line x1="186" y1="359" x2="840" y2="359"/><line x1="186" y1="395" x2="840" y2="395"/>
      <line x1="186" y1="430" x2="840" y2="430"/><line x1="186" y1="466" x2="840" y2="466"/>
      <line x1="186" y1="138" x2="186" y2="466"/>
    </g>
    <g fill="#fff" font-family="Arimo, Arial, sans-serif" font-size="12" font-weight="700" text-anchor="end">
      <text x="176" y="148">800</text><text x="176" y="184">600</text><text x="176" y="220">400</text>
      <text x="176" y="256">200</text><text x="176" y="291">100</text><text x="176" y="327">80</text>
      <text x="176" y="363">60</text><text x="176" y="399">40</text><text x="176" y="434">20</text>
      <text x="176" y="470">0</text>
    </g>
    <g>
      <rect x="192" y="450" width="24" height="16" fill="#fff"/>
      <rect x="260" y="288" width="24" height="178" fill="var(--bar-light)"/>
      <rect x="328" y="148" width="24" height="318" fill="#fff"/>
      <rect x="398" y="288" width="24" height="178" fill="var(--bar-light)"/>
      <rect x="466" y="254" width="24" height="212" fill="#fff"/>
      <rect x="534" y="254" width="24" height="212" fill="var(--bar-light)"/>
      <rect x="603" y="163" width="24" height="303" fill="#fff"/>
      <rect x="673" y="254" width="24" height="212" fill="var(--bar-light)"/>
      <rect x="741" y="217" width="24" height="249" fill="#fff"/>
      <rect x="811" y="270" width="24" height="196" fill="var(--bar-light)"/>
    </g>
    <g fill="#fff" font-family="Arimo, Arial, sans-serif" font-size="12.5" font-weight="700" text-anchor="middle">
      <text x="204" y="494">2012</text><text x="272" y="494">2013</text><text x="340" y="494">2014</text>
      <text x="410" y="494">2015</text><text x="478" y="494">2016</text><text x="546" y="494">2017</text>
      <text x="615" y="494">2018</text><text x="685" y="494">2019</text><text x="753" y="494">2020</text>
      <text x="823" y="494">2021</text>
    </g>
  </svg>
</section>

<!-- Pillars -->
<section class="slide s-pillars">
  <h2 class="section-title">NEMO ENIM IPSAM VOLUPTATEM</h2>
  <div class="photo" role="img" aria-label="Photograph of a team pointing at printed charts on a meeting table" style="left:312px;top:110px;width:363px;height:396px;background:linear-gradient(150deg,#5b5e62 0%,#a08f7c 50%,#6d5a4b 100%)"></div>
  <svg class="shape" viewBox="0 0 985 553" aria-hidden="true">
    <g fill="var(--slate)" stroke="#fff" stroke-width="3">
      <circle cx="315" cy="212" r="46"/><circle cx="675" cy="212" r="46"/>
      <circle cx="315" cy="405" r="46"/><circle cx="675" cy="405" r="46"/>
    </g>
    <g fill="none" stroke="#fff" stroke-width="2">
      <path d="M300 232v-14h7v14M311 232v-22h7v22M322 232v-30h7v30M298 212l14-10 6 4 12-10"/><circle cx="299" cy="226" r="6"/>
      <path d="M675 232v-16M675 222c-8 0-12-6-12-10 6 0 12 4 12 10zM675 222c8 0 12-6 12-10-6 0-12 4-12 10z"/><circle cx="675" cy="198" r="10"/><path d="M675 192v12M663 234h24"/>
      <rect x="297" y="388" width="36" height="34" rx="3"/><path d="M303 396h8M303 404h8M303 412h8M317 396h10M317 404h10M317 412h10"/>
      <path d="M678 388l-10 18h9l-6 16 14-21h-9l6-13"/><path d="M649 405h6M695 405h6M675 379v-5M675 436v-5M657 387l4 4M693 387l-4 4M657 423l4-4M693 423l-4-4"/>
    </g>
  </svg>
  <div class="pillar left" style="left:12px;top:177px">
    <h3>Sed ut perspiciatis unde omnis<br>iste natus error sits</h3>
    <p>Sed ut perspiciatis unde omnis iste natus error sit voluptatem accusantium doloremque laudantium totam rem aperiam, eaque ipsa quae ab illo.</p>
  </div>
  <div class="pillar" style="left:734px;top:177px">
    <h3>Sed ut perspiciatis unde omnis<br>iste natus error sits</h3>
    <p>Sed ut perspiciatis unde omnis iste natus error sit voluptatem accusantium doloremque laudantium totam rem aperiam, eaque ipsa quae ab illo.</p>
  </div>
  <div class="pillar left" style="left:12px;top:370px">
    <h3>Sed ut perspiciatis unde omnis<br>iste natus error sits</h3>
    <p>Sed ut perspiciatis unde omnis iste natus error sit voluptatem accusantium doloremque laudantium totam rem aperiam, eaque ipsa quae ab illo.</p>
  </div>
  <div class="pillar" style="left:734px;top:370px">
    <h3>Sed ut perspiciatis unde omnis<br>iste natus error sits</h3>
    <p>Sed ut perspiciatis unde omnis iste natus error sit voluptatem accusantium doloremque laudantium totam rem aperiam, eaque ipsa quae ab illo.</p>
  </div>
</section>

<!-- Closing -->
<section class="slide s-close">
  <div class="photo" role="img" aria-label="Photograph looking up at tall glass office towers" style="left:0;top:0;width:985px;height:553px;background:linear-gradient(120deg,#27313d 0%,#3f4a58 50%,#59626e 100%)"></div>
  <svg class="shape" viewBox="0 0 985 553" aria-hidden="true">
    <polygon points="0,0 830,0 798,72 0,72" fill="var(--stripe)"/>
    <polygon points="0,0 812,0 780,72 0,72" fill="var(--navy)"/>
    <polygon points="150,481 985,481 985,553 118,553" fill="var(--stripe)"/>
    <polygon points="168,481 985,481 985,553 136,553" fill="var(--navy)"/>
  </svg>
  <div class="wordmark" style="left:39px;width:358px;top:226px">
    <span class="wm-small">PROJECT</span>
    <span class="wm-large">MERIDEL</span>
  </div>
  <div class="thanks">
    <h2>THANK YOU!</h2>
    <p>Sed ut perspiciatis unde omnis iste natus error sit voluptatem accusantium doloremque laudantium, totam rem aperiam, eaque ipsa quae ab illo inventore veritatis et quasi architecto beatae vitae dicta sunt explicabo.</p>
  </div>
</section>

</body>
</html>
```